Computer consultant business card

Brimlo Software is a newly started computer consulting company. It's a small one-man company that provides mostly Velunix applications but also websites in collaboration with designers. I'm running this company on the side of full time university studies.

I want the final design to be clean and memorable. Be creative! :)

Some inspiration:
http://www.tavelpix.net/design/73519
http://www.tavelpix.net/design/2739566/business-card-design-by-quillbop
http://www.tavelpix.net/design/804613/business-card-design-by-lorvena-brukwaldsen

See attachment for my company logo.
Updates

I would like to thank everyone for submitting! I'll need a couple of days to review and ultimately select a design.

Target Market(s)

Non-technical entrepreneurs and small companies.

Industry/Entity Type

University

Requirements
Must have
• My company logo.
In any way, both colors from my logo.
First- and last name, e-mail and phone number.
Double-sided design.
Nice to have
• Something creative with the symbol in my logo

```html
<!DOCTYPE html>
<html lang="en">
<head>
<meta charset="utf-8">
<title>Brimlo Software – Business Card</title>
<link rel="stylesheet" href="https://fonts.googleapis.com/css2?family=Open+Sans:wght@400;600;700;800&display=swap">
<style>
  :root {
    --stage: #2b2b2d;
    --ink: #141414;
    --ink-soft: #1d1d1f;
    --brand-blue: #3a65b3;
    --paper: #f4f4f4;
    --paper-shade: #e2e2e2;
    --text-dark: #1b1b1b;
    --text-body: #2a2a2a;
    --white: #ffffff;
  }
  * { box-sizing: border-box; margin: 0; padding: 0; }
  html, body {
    width: 1200px; height: 900px; overflow: hidden;
    background: var(--stage);
    font-family: "Open Sans", Arial, sans-serif;
  }
  .canvas {
    position: relative; width: 1200px; height: 900px;
    display: flex; flex-direction: column; align-items: center; justify-content: center;
    gap: 60px;
  }
  .card {
    position: relative; width: 600px; height: 343px; overflow: hidden;
    box-shadow: 0 10px 30px rgba(0,0,0,.45);
  }

  /* Back side */
  .card-back { background: var(--ink-soft); }
  .card-back .texture {
    position: absolute; inset: 0;
    background: linear-gradient(160deg, #222224 0%, #121213 100%);
  }
  .back-brand {
    position: absolute; left: 130px; top: 118px;
    display: flex; align-items: center; gap: 22px;
  }
  .brand-dot {
    width: 92px; height: 92px; border-radius: 50%;
    background: var(--brand-blue);
  }
  .brand-lockup { display: flex; flex-direction: column; }
  .brand-name {
    font-weight: 700; color: var(--white);
    font-size: 74px; line-height: 1; letter-spacing: 1px;
  }
  .brand-tagline {
    font-weight: 700; color: var(--white);
    font-size: 13px; letter-spacing: 1.2px; text-transform: uppercase;
    margin-top: 6px;
  }

  /* Front side */
  .card-front { background: linear-gradient(170deg, var(--paper) 40%, var(--paper-shade) 100%); }
  .front-shapes { position: absolute; inset: 0; width: 600px; height: 343px; }
  .front-brand {
    position: absolute; right: 36px; top: 52px;
    display: flex; align-items: center; gap: 12px;
  }
  .front-brand .brand-dot { width: 50px; height: 50px; }
  .front-brand .brand-name { font-size: 44px; }
  .holder { position: absolute; left: 78px; top: 196px; }
  .holder-name { font-size: 20px; font-weight: 800; color: var(--text-dark); }
  .holder-role {
    font-size: 13px; font-weight: 800; color: var(--brand-blue);
    text-transform: uppercase; letter-spacing: .6px; margin-top: -2px;
  }
  .contact {
    position: absolute; display: flex; align-items: center; gap: 12px;
    font-size: 16px; color: var(--text-body);
  }
  .contact-email { left: 286px; top: 246px; }
  .contact-phone { left: 40px; top: 296px; }
  .contact-icon { width: 24px; height: 24px; flex: none; }
</style>
</head>
<body>
<main class="canvas">

  <section class="card card-back" aria-label="Card back">
    <div class="texture" role="img" aria-label="Fine dark woven texture"></div>
    <div class="back-brand">
      <span class="brand-dot"></span>
      <div class="brand-lockup">
        <span class="brand-name">brimlo</span>
        <span class="brand-tagline">Computer Consulting Company</span>
      </div>
    </div>
  </section>

  <section class="card card-front" aria-label="Card front">
    <svg class="front-shapes" viewBox="0 0 600 343" aria-hidden="true">
      <polygon points="0,90 548,212 600,22 600,46 556,236 0,100" fill="var(--brand-blue)"/>
      <polygon points="0,0 600,0 600,22 548,212 0,90" fill="var(--ink)"/>
    </svg>
    <div class="front-brand">
      <span class="brand-dot"></span>
      <span class="brand-name">brimlo</span>
    </div>

    <div class="holder">
      <p class="holder-name">Your Name</p>
      <p class="holder-role">Company Position</p>
    </div>

    <p class="contact contact-email">
      <svg class="contact-icon" viewBox="0 0 24 24" aria-hidden="true">
        <circle cx="12" cy="12" r="11" fill="var(--brand-blue)" stroke="#1c2f57" stroke-width="1.2"/>
        <rect x="6" y="8" width="12" height="8.5" rx="1" fill="var(--white)"/>
        <path d="M6 8.5 L12 13 L18 8.5" fill="none" stroke="var(--brand-blue)" stroke-width="1.2"/>
      </svg>
      name@brimlosoft.net
    </p>

    <p class="contact contact-phone">
      <svg class="contact-icon" viewBox="0 0 24 24" aria-hidden="true">
        <circle cx="12" cy="12" r="11" fill="var(--brand-blue)" stroke="#1c2f57" stroke-width="1.2"/>
        <path d="M8.2 6.5 L10.2 6.5 L11 9.5 L9.6 10.6 C10.4 12.3 11.7 13.6 13.4 14.4 L14.5 13 L17.5 13.8 L17.5 15.8 C17.5 16.6 16.8 17.3 16 17.2 C11.2 16.8 7.2 12.8 6.8 8 C6.7 7.2 7.4 6.5 8.2 6.5 Z" fill="var(--white)"/>
      </svg>
      040 718 294
    </p>
  </section>

</main>
</body>
</html>
```